Logistics Website Design

See website https://tvarfreightglobal.com for theme and color details. Need the site to be re-done and reflect some of the designs shown in this list here: https://pinvora.com/tags/logistics-company-website

Target Market(s)

Logistics & Transportation

Industry/Entity Type

Logistics and Supply Chain

Coding

Coded - Design and coding required

Number of Pages Required

5+ page

Requirements
Must have
• Colors must match theme of logo. Looking for a sleek, interactive design.

```html
<!DOCTYPE html>
<html lang="en">
<head>
<meta charset="utf-8">
<title>Tvar Freight Global</title>
<link href="https://fonts.googleapis.com/css2?family=Montserrat:wght@500;600;700;800;900&family=Nunito+Sans:wght@400;600;700&display=swap" rel="stylesheet">
<style>
:root{
  --orange:#e8663d;
  --orange-dark:#d4552e;
  --ink:#111111;
  --text:#333333;
  --blush:#fdf3f0;
  --cream:#fdf1e6;
  --footer:#1a0c09;
  --white:#ffffff;
}
*{margin:0;padding:0;box-sizing:border-box}
html,body{width:1200px;height:3168px;overflow:hidden}
body{position:relative;background:var(--white);font-family:"Nunito Sans",sans-serif;color:var(--text)}
.abs{position:absolute}
.head-font{font-family:"Montserrat",sans-serif}
.btn{position:absolute;background:var(--orange);color:var(--white);font-family:"Montserrat",sans-serif;font-weight:800;display:flex;align-items:center;justify-content:center;gap:12px;border-radius:4px;text-transform:uppercase}
.btn svg{width:10px;height:16px}

/* header */
.site-header{position:absolute;left:0;top:0;width:1200px;height:86px;background:var(--white);z-index:3}
.brand{position:absolute;left:148px;top:14px;width:136px;height:126px;border-radius:50%;background:var(--white);display:flex;align-items:center;justify-content:center;z-index:4;box-shadow:0 2px 6px rgba(0,0,0,.08)}
.brand span{font-family:"Montserrat",sans-serif;font-weight:800;font-size:15px;color:var(--orange);text-align:center;line-height:1.15}
.nav{position:absolute;top:34px;font-family:"Montserrat",sans-serif;font-weight:500;font-size:13px;color:var(--ink)}
.nav.active{color:var(--orange)}
.nav-bar{position:absolute;left:361px;top:80px;width:54px;height:6px;background:var(--orange)}
.header-btn{left:869px;top:20px;width:178px;height:45px;font-size:12.5px}

/* hero */
.hero{position:absolute;left:0;top:86px;width:1200px;height:584px;background:linear-gradient(100deg,#3d4a2a 0%,#5f6d3c 30%,#8a9670 55%,#b7bcb3 75%,#8e7f72 100%)}
.hero-title{position:absolute;left:148px;top:200px;font-family:"Montserrat",sans-serif;font-weight:900;font-size:55px;line-height:57px;color:var(--white);text-transform:uppercase}
.hero-title em{font-style:normal;color:var(--orange)}
.hero-sub{position:absolute;left:151px;top:386px;width:380px;font-family:"Montserrat",sans-serif;font-weight:700;font-size:26px;line-height:33px;color:var(--white)}
.hero-btn{left:152px;top:518px;width:210px;height:49px;font-size:15px}
.dots{position:absolute;left:560px;top:631px;display:flex;gap:8px}
.dots i{display:block;width:13px;height:4px;background:var(--white);border-radius:2px}
.dots i.on{background:var(--orange)}

/* section heading */
.sec-title{position:absolute;left:0;width:1200px;text-align:center;font-family:"Montserrat",sans-serif;font-weight:800;font-size:32px;color:var(--ink)}
.rule{position:absolute;height:3px;width:40px;background:var(--orange)}

/* services */
.service{position:absolute;top:840px;width:286px;height:400px;border-radius:8px;overflow:hidden;background:linear-gradient(180deg,#dfe7f3 0%,#eef1f6 45%,#a9b3a4 75%,#747466 100%)}
.service h3{position:absolute;left:30px;top:30px;font-family:"Montserrat",sans-serif;font-size:16.5px;line-height:22px;font-weight:600;color:var(--ink)}
.service h3 b{color:var(--orange);font-weight:700;display:block}
.service p{position:absolute;left:30px;top:84px;width:230px;font-size:11.5px;line-height:16.5px;color:#333}
.service .btn{left:30px;top:152px;width:94px;height:30px;font-size:10px}

/* about */
.about{position:absolute;left:0;top:1298px;width:1200px;height:531px;background:var(--blush)}
.about-photo{position:absolute;left:149px;top:1352px;width:458px;height:430px;border-radius:8px;background:linear-gradient(170deg,#dfe8f2 0%,#c2cdd0 40%,#9e7d6a 62%,#7b7a74 100%)}
.about-title{position:absolute;left:657px;top:1365px;font-family:"Montserrat",sans-serif;font-weight:800;font-size:33px;line-height:40px;color:var(--ink)}
.about-title em{font-style:normal;color:var(--orange)}
.about-text{position:absolute;left:657px;top:1505px;width:395px;font-size:14.5px;line-height:24px;color:#333}
.about-btn{left:659px;top:1709px;width:143px;height:49px;font-size:14px}

/* industries */
.industry{position:absolute;top:2025px;width:216px;height:174px;border-radius:8px;background:linear-gradient(180deg,#fffaf6 0%,var(--cream) 100%);box-shadow:0 2px 8px rgba(232,102,61,.08)}
.industry svg{position:absolute;left:50%;top:34px;transform:translateX(-50%);width:50px;height:50px}
.industry span{position:absolute;left:0;top:112px;width:100%;text-align:center;font-family:"Montserrat",sans-serif;font-weight:500;font-size:13.5px;line-height:21px;color:var(--ink)}
.industry.active{background:var(--orange)}
.industry.active span{color:var(--white)}
.arrow-circ{position:absolute;top:2093px;width:30px;height:30px;border:1.5px solid #555;border-radius:50%;display:flex;align-items:center;justify-content:center}

/* quote */
.quote{position:absolute;left:0;top:2270px;width:1200px;height:506px;background:var(--blush)}
.badge{position:absolute;left:150px;top:2334px;padding:5px 16px;background:var(--white);border-radius:4px;font-family:"Montserrat",sans-serif;font-weight:500;font-size:13.5px;color:var(--ink)}
.quote-title{position:absolute;left:149px;top:2383px;font-family:"Montserrat",sans-serif;font-weight:800;font-size:32px;line-height:38px;color:var(--ink)}
.quote-title em{font-style:normal;color:var(--orange)}
.quote-text{position:absolute;left:149px;top:2588px;width:400px;font-size:13.5px;line-height:21px}
.call{position:absolute;left:149px;top:2660px;display:flex;align-items:center;gap:14px}
.call small{display:block;font-family:"Montserrat",sans-serif;font-weight:500;font-size:13px;color:var(--ink)}
.call strong{display:block;font-family:"Montserrat",sans-serif;font-weight:500;font-size:19px;color:var(--orange)}
.form-card{position:absolute;left:588px;top:2330px;width:464px;height:394px;background:var(--white);border-radius:8px}
.field{position:absolute;left:29px;width:405px;border:1px solid #888;border-radius:6px;font-size:12px;color:#444;padding:13px 20px}
.send-btn{left:620px;top:2645px;width:158px;height:45px;font-size:13.5px}

/* footer */
.site-footer{position:absolute;left:0;top:2776px;width:1200px;height:392px;background:var(--footer)}
.foot-brand{position:absolute;left:149px;top:2832px;width:188px;height:168px;border-radius:50%;border:2px solid var(--orange);display:flex;align-items:center;justify-content:center}
.foot-brand span{font-family:"Montserrat",sans-serif;font-weight:800;font-size:20px;color:var(--orange);text-align:center;line-height:1.2}
.foot-col{position:absolute;top:2834px}
.foot-col h4{font-family:"Montserrat",sans-serif;font-weight:700;font-size:13px;color:var(--white);margin-bottom:16px}
.foot-col a{display:block;font-size:13.5px;line-height:30px;color:var(--white);text-decoration:none}
.foot-rule{position:absolute;left:149px;top:3055px;width:902px;height:1px;background:#4a2015}
.copyright{position:absolute;left:0;top:3100px;width:1200px;text-align:center;font-size:13.5px;color:var(--white)}
</style>
</head>
<body>

<header class="site-header">
  <span class="nav active" style="left:367px">HOME</span>
  <span class="nav" style="left:440px">ABOUT US</span>
  <span class="nav" style="left:543px">SERVICES</span>
  <span class="nav" style="left:641px">INDUSTRIES</span>
  <span class="nav" style="left:754px">CONTACT US</span>
  <div class="nav-bar"></div>
  <a class="btn header-btn">Request a quote <svg viewBox="0 0 10 16"><path d="M2 2l6 6-6 6" fill="none" stroke="#fff" stroke-width="2.4"/></svg></a>
</header>
<div class="brand"><span>TVAR<br>FREIGHT</span></div>

<section class="hero" role="img" aria-label="Silver semi truck hauling a covered flatbed load on a highway lined with green trees"></section>
<h1 class="hero-title">Delivering<br><em>Strength</em> in<br>every mile</h1>
<p class="hero-sub">Secure and reliable transportation for all your cargo needs.</p>
<a class="btn hero-btn">Request a quote <svg viewBox="0 0 10 16"><path d="M2 2l6 6-6 6" fill="none" stroke="#fff" stroke-width="2.4"/></svg></a>
<div class="dots"><i class="on"></i><i></i><i></i><i></i></div>

<h2 class="sec-title" style="top:720px">OUR SERVICES</h2>
<div class="rule" style="left:580px;top:786px"></div>

<article class="service" style="left:10px" role="img" aria-label="White semi truck with flatbed load under a blue sky">
  <h3><b>FLATBED</b>TRANSPORTATION</h3>
  <p>From routine shipments to oversized and heavy-haul loads, we handle freight requiring proper securement</p>
  <a class="btn">Read more</a>
</article>
<article class="service" style="left:309px" role="img" aria-label="Black truck pulling an empty step deck trailer through farmland">
  <h3><b>STEP DECK</b>TRANSPORTATION</h3>
  <p>Our step deck trucking services support tall, heavy, and specialized freight that requires additional height clearance</p>
  <a class="btn">Read more</a>
</article>
<article class="service" style="left:607px" role="img" aria-label="Red semi truck with a white dry van trailer on the road">
  <h3><b>DRY VAN</b>TRANSPORTATION</h3>
  <p>From consumer goods to industrial materials, our dry van services provide the space, security, and consistency</p>
  <a class="btn">Read more</a>
</article>
<article class="service" style="left:905px" role="img" aria-label="Red heavy haul truck with a livestock trailer under clouds">
  <h3><b>HEAVY HAUL</b>TRANSPORTATION</h3>
  <p>We provide heavy haul trucking solutions for oversized, overweight, and over-dimensional freight.</p>
  <a class="btn">Read more</a>
</article>

<section class="about"></section>
<div class="about-photo" role="img" aria-label="Red semi truck hauling a flatbed of lumber on a sunny highway"></div>
<h2 class="about-title">KEEPING YOUR SUPPLY<br><em>CHAIN MOVING</em></h2>
<div class="rule" style="left:657px;top:1467px"></div>
<p class="about-text">We deliver a comprehensive range of open-deck and specialized transportation services—including flatbed, step deck, heavy haul, and over-dimensional freight solutions. Backed by years of experience, a trusted nationwide carrier network, and a strong safety-first culture, we provide reliable, adaptable logistics support built around the unique requirements of every load.</p>
<a class="btn about-btn">Read more <svg viewBox="0 0 10 16"><path d="M2 2l6 6-6 6" fill="none" stroke="#fff" stroke-width="2.4"/></svg></a>

<h2 class="sec-title" style="top:1890px">INDUSTRIES</h2>
<div class="rule" style="left:580px;top:1960px"></div>

<div class="arrow-circ" style="left:77px"><svg width="10" height="12" viewBox="0 0 10 12"><path d="M7 1L2 6l5 5" fill="none" stroke="#555" stroke-width="1.5"/></svg></div>
<div class="arrow-circ" style="left:1088px"><svg width="10" height="12" viewBox="0 0 10 12"><path d="M3 1l5 5-5 5" fill="none" stroke="#555" stroke-width="1.5"/></svg></div>

<div class="industry" style="left:149px">
  <svg viewBox="0 0 50 50" fill="none" stroke="#e8663d" stroke-width="1.8"><path d="M8 22h18l-2 20H10z"/><path d="M17 22V10l6-4"/><path d="M28 30h16M28 38h16M29 30c0-5 14-5 14 0M28 38v4h16v-4"/></svg>
  <span>FOOD &amp;<br>BEVERAGE</span>
</div>
<div class="industry active" style="left:380px">
  <svg viewBox="0 0 50 50" fill="none" stroke="#fff" stroke-width="1.8"><rect x="8" y="6" width="22" height="38" rx="3"/><path d="M14 16h10M14 24h10"/><rect x="24" y="22" width="20" height="16" rx="2"/><path d="M28 28h12l-2 6h-8z"/></svg>
  <span>E-COMMERCE &amp;<br>RETAIL</span>
</div>
<div class="industry" style="left:608px">
  <svg viewBox="0 0 50 50" fill="none" stroke="#e8663d" stroke-width="1.8"><rect x="10" y="6" width="16" height="6"/><rect x="8" y="12" width="20" height="30" rx="3"/><path d="M18 22v10M13 27h10"/><rect x="26" y="30" width="18" height="9" rx="4.5" transform="rotate(-30 35 34)"/></svg>
  <span>PHARMA &amp;<br>HEALTHCARE</span>
</div>
<div class="industry" style="left:835px">
  <svg viewBox="0 0 50 50" fill="none" stroke="#e8663d" stroke-width="1.8"><path d="M6 16L25 6l19 10z"/><path d="M8 18h34M11 20v18M19 20v18M31 20v18M39 20v18M6 40h38M4 44h42"/></svg>
  <span>GOVERNMENT<br>SECURED FREIGHT</span>
</div>

<section class="quote"></section>
<div class="badge">FREE QUOTE</div>
<h2 class="quote-title">GET A <em>FREE ESTIMATE</em><br>OUR SCHEDULE AN<br>APPOINTMENT<br>WITH US</h2>
<div class="rule" style="left:149px;top:2555px"></div>
<p class="quote-text">Lorem ipsum dolor sit amet, consectetur adipiscing elit, sed do eiusmod tempor incididunt ut labore et dolore.</p>
<div class="call">
  <svg width="34" height="34" viewBox="0 0 34 34" fill="none" stroke="#e8663d" stroke-width="1.5"><circle cx="17" cy="17" r="16"/><path d="M11 9l4 4-2 3c1 3 3 5 6 6l3-2 4 4-3 3c-7 0-15-8-15-15z"/></svg>
  <div><small>CALL US</small><strong>+1 555 014 2290</strong></div>
</div>

<form class="form-card">
  <div class="field" style="top:40px;height:42px">Name</div>
  <div class="field" style="top:98px;height:42px">Email</div>
  <div class="field" style="top:155px;height:135px">Message</div>
</form>
<a class="btn send-btn">Send message</a>

<footer class="site-footer"></footer>
<div class="foot-brand"><span>TVAR<br>FREIGHT<br>GLOBAL</span></div>
<div class="foot-col" style="left:438px"><h4>MENU</h4><a>Flatbed</a><a>Step Deck</a><a>Dry Van</a><a>Heavy Haul</a></div>
<div class="foot-col" style="left:645px"><h4>INDUSTRIES</h4><a>Food &amp; beverage</a><a>E-commerce &amp; retail</a><a>Manufacturing</a><a>Pharma &amp; healthcare</a><a>Government</a></div>
<div class="foot-col" style="left:907px"><h4>REQUEST A QUOTE</h4><a>Contact</a><a>Company</a><a>Project</a></div>
<div class="foot-rule"></div>
<p class="copyright">© 2026. An independent agent of Halvern Crane LLC.</p>

</body>
</html>
```